Oil and Gas Exploration and Production company needs a business card design

We need a business card design using our logo and colors in the logo. We want a mainstream design.

```html
<!DOCTYPE html>
<html lang="en">
<head>
<meta charset="utf-8">
<title>Kora Oil &amp; Gas – Business Card</title>
<link rel="stylesheet" href="https://fonts.googleapis.com/css2?family=PT+Serif:wght@700&display=swap">
<style>
  :root {
    --ink: #050505;
    --paper: #ffffff;
    --gold: #c99a3b;
    --text-light: #ffffff;
    --serif: "PT Serif", Georgia, serif;
  }
  * { margin: 0; padding: 0; box-sizing: border-box; }
  html, body { width: 1200px; height: 686px; overflow: hidden; background: var(--paper); }
  .card {
    position: relative;
    width: 1200px;
    height: 686px;
    background: var(--paper);
    font-family: var(--serif);
    font-weight: 700;
    overflow: hidden;
  }
  .card__backdrop { position: absolute; inset: 0; }

  .brand {
    position: absolute;
    left: 48px; top: 100px;
    display: flex;
    align-items: center;
    gap: 26px;
  }
  .brand__mark {
    width: 70px; height: 70px;
    border-radius: 50%;
    background: var(--gold);
    flex: none;
  }
  .brand__name {
    color: var(--ink);
    font-size: 76px;
    line-height: 1;
    white-space: nowrap;
  }

  .divider {
    position: absolute;
    left: 535px; top: 352px;
    width: 4px; height: 296px;
    background: var(--text-light);
  }

  .person {
    position: absolute;
    left: 63px; width: 400px; top: 424px;
    text-align: center;
    color: var(--text-light);
  }
  .person__name { font-size: 43px; line-height: 1; }
  .person__role { font-size: 21px; margin-top: 14px; letter-spacing: 0.5px; }

  .contact {
    position: absolute;
    right: 135px;
    text-align: right;
    color: var(--text-light);
    font-size: 35px;
    line-height: 46px;
  }
  .contact--phone { top: 322px; }
  .contact--web { top: 442px; }
  .contact--address { top: 568px; }

  .icon { position: absolute; left: 1109px; width: 56px; height: 56px; }
  .icon--phone { top: 338px; }
  .icon--web { top: 458px; }
  .icon--pin { top: 580px; }
</style>
</head>
<body>
<div class="card">
  <svg class="card__backdrop" width="1200" height="686" viewBox="0 0 1200 686" aria-hidden="true">
    <polygon points="0,281 683,281 1200,0 1200,686 0,686" fill="var(--ink)"/>
  </svg>

  <div class="brand">
    <div class="brand__mark"></div>
    <p class="brand__name">Kora Oil &amp; Gas</p>
  </div>

  <div class="divider"></div>

  <div class="person">
    <p class="person__name">Lena Ward</p>
    <p class="person__role">MANAGER</p>
  </div>

  <div class="contact contact--phone">
    <p>+003875550148</p>
    <p>+003985550172</p>
  </div>
  <div class="contact contact--web">
    <p>lena.ward@kora.com</p>
    <p>www.kora.com</p>
  </div>
  <div class="contact contact--address">
    <p>210,Oak Avenue</p>
    <p>Dallas, USA 7521</p>
  </div>

  <svg class="icon icon--phone" viewBox="0 0 24 24" aria-hidden="true">
    <path fill="#fff" d="M6.6 10.8a15.1 15.1 0 0 0 6.6 6.6l2.2-2.2a1 1 0 0 1 1-.25 11.4 11.4 0 0 0 3.6.57 1 1 0 0 1 1 1V20a1 1 0 0 1-1 1A17 17 0 0 1 3 4a1 1 0 0 1 1-1h3.5a1 1 0 0 1 1 1c0 1.25.2 2.45.57 3.57a1 1 0 0 1-.25 1z"/>
  </svg>
  <svg class="icon icon--web" viewBox="0 0 24 24" aria-hidden="true">
    <g fill="none" stroke="#fff" stroke-width="1.2">
      <circle cx="12" cy="12" r="10"/>
      <ellipse cx="12" cy="12" rx="4.5" ry="10"/>
      <line x1="12" y1="2" x2="12" y2="22"/>
      <line x1="2" y1="12" x2="22" y2="12"/>
      <path d="M3.8 7h16.4M3.8 17h16.4"/>
    </g>
  </svg>
  <svg class="icon icon--pin" viewBox="0 0 24 24" aria-hidden="true">
    <path fill="#fff" fill-rule="evenodd" d="M12 1.5a7.5 7.5 0 0 0-7.5 7.5c0 5.6 7.5 13.5 7.5 13.5s7.5-7.9 7.5-13.5A7.5 7.5 0 0 0 12 1.5zm0 4.5a3 3 0 1 1 0 6 3 3 0 0 1 0-6z"/>
  </svg>
</div>
</body>
</html>
```